Stationary Design using supplied logo

24 Hour Completion required after acceptance

Business Cards
Letter Head
With Compliments Slips
Web Page Theme

Please only use a the following colors:

Red
Charcoal
Chrome/Silver
White

Red being the DOMINANT Color

Please email questions you may have.

Continued work available to suitably motivated designer.

Industry/Entity Type

Business

```html
<!DOCTYPE html>
<html lang="en">
<head>
<meta charset="utf-8">
<title>nova funds — stationery set</title>
<link rel="stylesheet" href="https://fonts.googleapis.com/css2?family=Raleway:wght@300;400;600;700&display=swap">
<style>
:root{
  --red:#c8202f;
  --charcoal:#434345;
  --charcoal-dark:#363638;
  --silver:#d9d9db;
  --paper:#f4f4f4;
  --bg:#e9e9ea;
  --ink:#58585a;
  --watermark:rgba(0,0,0,.045);
}
*{box-sizing:border-box;margin:0;padding:0}
html,body{width:1200px;height:859px;overflow:hidden}
body{background:var(--bg);font-family:"Raleway",sans-serif;color:var(--ink);position:relative}
.piece{position:absolute;background:var(--paper);box-shadow:0 2px 6px rgba(0,0,0,.12);overflow:hidden}

/* brand block */
.brand{display:flex;flex-direction:column;align-items:flex-end}
.brand-name{display:flex;align-items:center;gap:.25em;color:var(--red);font-weight:300;line-height:1;letter-spacing:.01em}
.brand-dot{width:.42em;height:.42em;border-radius:50%;background:var(--red)}
.brand-tagline{font-weight:600;letter-spacing:.28em;text-transform:uppercase;color:var(--ink);margin-top:.3em}

.watermark{position:absolute;border-radius:50%;background:var(--watermark)}

/* business cards */
.card{width:220px;height:126px}
.card-front{left:40px;top:70px}
.card-back{left:40px;top:216px;background:var(--charcoal);display:flex;align-items:center;justify-content:center}
.card-front .brand{position:absolute;right:14px;top:18px}
.card-front .brand-name{font-size:22px}
.card-front .brand-tagline{font-size:4.5px}
.card-person{position:absolute;left:14px;top:58px}
.card-person .name{font-size:8px;font-weight:700;letter-spacing:.08em;text-transform:uppercase;color:var(--ink)}
.card-person .role{font-size:6px;color:var(--red);margin-top:2px}
.card-contact{position:absolute;left:14px;bottom:14px;font-size:5.5px;line-height:1.6;display:grid;grid-template-columns:auto auto;column-gap:18px}
.card-contact b{color:var(--red);font-weight:700;margin-right:3px}
.card-back .brand{align-items:center}
.card-back .brand-name{font-size:28px}
.card-back .brand-tagline{font-size:5.5px;color:var(--silver)}

/* letterhead */
.letterhead{left:290px;top:40px;width:300px;height:424px}
.letterhead .watermark{left:-40px;top:-70px;width:210px;height:210px}
.letterhead .brand{position:absolute;right:24px;top:26px}
.letterhead .brand-name{font-size:26px}
.letterhead .brand-tagline{font-size:5px}
.letterhead-footer{position:absolute;left:18px;right:18px;bottom:26px;display:flex;justify-content:space-between;font-size:5.2px;line-height:1.7}
.letterhead-footer b,.slip-address b,.envelope-address b{color:var(--red);font-weight:700;text-transform:uppercase;margin-right:3px}
.band{position:absolute;left:0;right:0;bottom:0;height:8px;display:flex}
.band .seg-red{background:var(--red)}
.band .seg-dark{background:var(--charcoal)}

/* compliments slip */
.slip{left:40px;top:512px;width:440px;height:208px}
.slip .watermark{right:30px;top:70px;width:170px;height:170px}
.slip .brand{position:absolute;left:110px;top:26px}
.slip .brand-name{font-size:28px}
.slip .brand-tagline{font-size:5.5px}
.slip-address{position:absolute;left:16px;bottom:90px;font-size:5.5px}
.slip .band{bottom:78px;height:8px}

/* presentation folder */
.folder{left:640px;top:40px;width:350px;height:494px}
.folder .brand{position:absolute;right:26px;top:52px}
.folder .brand-name{font-size:38px}
.folder .brand-tagline{font-size:7px}
.folder .band{bottom:auto;top:150px;height:9px}
.folder-panel{position:absolute;left:0;right:0;top:159px;bottom:0;background:var(--charcoal)}
.folder-panel .watermark{left:70px;top:60px;width:260px;height:260px;background:rgba(0,0,0,.1)}

/* envelope */
.envelope{left:560px;top:574px;width:440px;height:222px}
.envelope-flap{position:absolute;left:0;top:0;width:100%;height:110px}
.envelope-seal{position:absolute;left:212px;top:60px;width:16px;height:16px;border-radius:50%;background:var(--red)}
.envelope-address{position:absolute;left:18px;right:18px;bottom:22px;display:flex;justify-content:space-between;font-size:6px}
.envelope-address .sep{color:var(--silver)}
</style>
</head>
<body>

<!-- business card, front -->
<section class="piece card card-front">
  <div class="brand">
    <div class="brand-name">nova funds<span class="brand-dot"></span></div>
    <div class="brand-tagline">Saving Made Simple</div>
  </div>
  <div class="card-person">
    <div class="name">Daniel Hart</div>
    <div class="role">Finance Manager</div>
  </div>
  <div class="card-contact">
    <span><b>P</b>02 6100 1000</span><span><b>E</b>info@novafunds.com.au</span>
    <span><b>M</b>0400 100 200</span><span><b>W</b>novafunds.com.au</span>
  </div>
</section>

<!-- business card, back -->
<section class="piece card card-back">
  <div class="brand">
    <div class="brand-name">nova funds<span class="brand-dot"></span></div>
    <div class="brand-tagline">Saving Made Simple</div>
  </div>
</section>

<!-- letterhead -->
<section class="piece letterhead">
  <div class="watermark" role="img" aria-label="faint brand symbol watermark"></div>
  <div class="brand">
    <div class="brand-name">nova funds<span class="brand-dot"></span></div>
    <div class="brand-tagline">Saving Made Simple</div>
  </div>
  <div class="letterhead-footer">
    <div>
      <div><b>Head Office</b>Marlow St Eastfield</div>
      <div><b>Northgate</b>Cnr Reed St &amp; Carver Cres Holm</div>
      <div><b>Westvale</b>Penrose Chambers Westvale</div>
    </div>
    <div>
      <div><b>P</b>02 6100 1000</div>
      <div><b>F</b>02 6100 1001</div>
    </div>
    <div>
      <div><b>E</b>info@novafunds.com.au</div>
      <div><b>W</b>www.novafunds.com.au</div>
    </div>
  </div>
  <div class="band"><span class="seg-red" style="width:36%"></span><span class="seg-dark" style="width:64%"></span></div>
</section>

<!-- compliments slip -->
<section class="piece slip">
  <div class="watermark" role="img" aria-label="faint brand symbol watermark"></div>
  <div class="brand">
    <div class="brand-name">nova funds<span class="brand-dot"></span></div>
    <div class="brand-tagline">Saving Made Simple</div>
  </div>
  <div class="slip-address">PO Box 4100 Eastfield 2600</div>
  <div class="band"><span class="seg-dark" style="width:33%"></span><span class="seg-red" style="width:67%"></span></div>
</section>

<!-- presentation folder -->
<section class="piece folder">
  <div class="brand">
    <div class="brand-name">nova funds<span class="brand-dot"></span></div>
    <div class="brand-tagline">Saving Made Simple</div>
  </div>
  <div class="band"><span class="seg-dark" style="width:24%"></span><span class="seg-red" style="width:76%"></span></div>
  <div class="folder-panel">
    <div class="watermark" role="img" aria-label="large faint brand symbol decoration"></div>
  </div>
</section>

<!-- envelope, back -->
<section class="piece envelope">
  <svg class="envelope-flap" viewBox="0 0 440 110" preserveAspectRatio="none" aria-hidden="true">
    <polygon points="0,0 440,0 440,110 0,62" fill="var(--charcoal)"/>
  </svg>
  <div class="envelope-seal"></div>
  <div class="envelope-address">
    <span><b>Head Office</b>Marlow St Eastfield</span>
    <span class="sep">|</span>
    <span><b>Northgate</b>Cnr Reed St &amp; Carver Cres Holm</span>
    <span class="sep">|</span>
    <span><b>Westvale</b>Penrose Chambers Westvale</span>
  </div>
</section>

</body>
</html>
```